Freshen up Product Labels

We need product label designs refreshed throughout our brand. We will start with the main product as that will set the basic design for most other labels. We are currently using 2.5" wide x 4.5" tall vinyl labels for most products and would like to stick to that size for this project. There are 3 of this size label on a jug of our all natural house cleaning concentrate. Uploaded current design and open to your new ideas. Our products can be found in more detail at voldrimo.com

```html
<!DOCTYPE html>
<html lang="en">
<head>
<meta charset="utf-8">
<title>Voldrimo Aromatheraphy Cleaning Concentrate – Labels</title>
<link rel="stylesheet" href="https://fonts.googleapis.com/css2?family=Gilda+Display&family=Playfair+Display:wght@600;700&family=Montserrat:wght@400;500;600;700&display=swap">
<style>
  :root{
    --bg:#efefef;
    --paper:#ffffff;
    --green:#57b346;
    --deep-green:#2f9a4f;
    --lime:#a9c93b;
    --leaf-soft:#cfe9c6;
    --leaf-grey:#e3e3e3;
    --ink:#1d1d1d;
    --rule:#8a8a8a;
    --cross:#d8342b;
  }
  *{box-sizing:border-box;margin:0;padding:0}
  html,body{width:746px;height:1200px;overflow:hidden}
  body{background:var(--bg);font-family:"Montserrat",sans-serif;color:var(--ink);position:relative}

  .label{position:absolute;top:320px;width:350px;height:560px;background:var(--paper);overflow:hidden;box-shadow:0 6px 18px rgba(0,0,0,.10)}
  .label--front{left:15px}
  .label--back{left:381px}

  .foliage{position:absolute;border-radius:50%;filter:blur(2px)}
  .foliage--soft{background:radial-gradient(closest-side,var(--leaf-soft),rgba(207,233,198,0))}
  .foliage--grey{background:radial-gradient(closest-side,var(--leaf-grey),rgba(227,227,227,0))}
  .foliage--green{background:radial-gradient(closest-side,#7cc465,rgba(124,196,101,0))}

  /* front */
  .brand{position:absolute;top:62px;left:0;width:100%;text-align:center}
  .brand__dot{display:block;width:22px;height:22px;border-radius:50%;background:var(--green);margin:0 auto 8px}
  .brand__name{font-family:"Montserrat",sans-serif;font-weight:700;font-size:26px;letter-spacing:1px;color:var(--green)}
  .title-small{position:absolute;top:158px;width:100%;text-align:center;font-family:"Gilda Display",serif;font-size:30px}
  .title-main{position:absolute;top:180px;width:100%;text-align:center;font-family:"Playfair Display",serif;font-weight:700;font-size:66px;color:var(--lime);letter-spacing:-1px;line-height:1}
  .concentrate{position:absolute;top:263px;left:85px;width:180px;height:34px;background:var(--deep-green);clip-path:polygon(0 0,100% 0,95% 50%,100% 100%,0 100%,5% 50%);color:#fff;font-weight:500;font-size:14px;letter-spacing:3.6px;text-align:center;line-height:34px}
  .oils-rule{position:absolute;top:316px;left:54px;width:243px;height:26px;border-top:1px solid var(--rule);border-bottom:1px solid var(--rule);text-align:center;font-size:8.6px;font-weight:500;letter-spacing:2.1px;color:var(--green);line-height:24px}
  .scents{position:absolute;top:376px;width:100%;text-align:center;font-family:"Gilda Display",serif;font-size:14px;line-height:17px}
  .formula{position:absolute;top:438px;width:100%;text-align:center;font-size:8.6px;font-weight:500;color:var(--green);line-height:11.5px}
  .base-band{position:absolute;left:0;bottom:0;width:100%;height:40px;background:var(--green)}
  .yield-badge{position:absolute;left:129px;top:482px;width:92px;height:92px}

  /* back */
  .story{position:absolute;top:0;left:0;width:350px;height:189px;background:var(--green);border-bottom-right-radius:64px;color:#fff;padding:26px 22px 0 24px;font-size:10.6px;line-height:14.7px}
  .story p+p{margin-top:14.7px}
  .story strong{font-weight:600}
  .claims{position:absolute;top:205px;left:24px;width:304px;height:140px}
  .claims__col{position:absolute;top:0}
  .claims__col--yes{left:0}
  .claims__col--no{left:165px}
  .claims__divider{position:absolute;left:151px;top:2px;width:1px;height:130px;background:var(--ink)}
  .claims__head{font-family:"Gilda Display",serif;font-size:21px;line-height:26px;margin-bottom:6px}
  .claims__col--yes .claims__head{color:var(--lime)}
  .claims__col--no .claims__head{color:var(--deep-green)}
  .claims__list{list-style:none;font-family:"Gilda Display",serif;font-size:9.4px;line-height:15.6px;font-weight:600}
  .claims__list li{display:flex;align-items:center;gap:4px;white-space:nowrap}
  .claims__list svg{flex:none}
  .back-rule{position:absolute;top:352px;left:24px;width:304px;height:1px;background:var(--rule)}
  .ingredients{position:absolute;top:361px;left:24px;width:306px;font-size:10.6px;line-height:14.7px}
  .ingredients strong{font-weight:600}
  .warning{position:absolute;top:493px;left:24px;width:310px;font-size:10.6px;line-height:14.7px}
</style>
</head>
<body>

<section class="label label--front" aria-label="Front label">
  <div class="foliage foliage--grey" role="img" aria-label="Grey leaf sprigs" style="right:-30px;top:20px;width:140px;height:110px"></div>
  <div class="foliage foliage--soft" role="img" aria-label="Pale green leaf sprigs" style="left:-40px;top:90px;width:120px;height:150px"></div>
  <div class="foliage foliage--green" role="img" aria-label="Green leaf sprig" style="right:-30px;top:395px;width:90px;height:100px"></div>
  <div class="foliage foliage--soft" role="img" aria-label="Pale green leaf sprigs" style="left:-10px;top:440px;width:130px;height:90px"></div>

  <div class="brand"><span class="brand__dot"></span><span class="brand__name">VOLDRIMO</span></div>
  <h1 class="title-small">Aromatheraphy</h1>
  <div class="title-main">Cleaning</div>
  <div class="concentrate">CONCENTRATE</div>
  <div class="oils-rule">CONTAINS POWERFUL ESSENTIAL OILS</div>
  <p class="scents">cinnamon + clove + lemon<br>rosemary + peppermint + eucalyptus</p>
  <p class="formula">ULTRA CONCENTARTED<br>VERSATILE FORMULA</p>

  <div class="base-band"></div>
  <svg class="yield-badge" viewBox="0 0 92 92" aria-label="makes 24 gallons of cleaner, 64oz">
    <circle cx="46" cy="46" r="46" fill="#ffffff"/>
    <defs><path id="badge-arc" d="M18 74 A36 36 0 1 1 74 74"/></defs>
    <text font-family="Montserrat, sans-serif" font-size="9" fill="#57b346" letter-spacing="0.6">
      <textPath href="#badge-arc">makes 24 gallons of cleaner</textPath>
    </text>
    <text x="46" y="50" text-anchor="middle" font-family="Gilda Display, serif" font-size="15" fill="#57b346">64oz</text>
  </svg>
</section>

<section class="label label--back" aria-label="Back label">
  <div class="story">
    <p>Turn the mundane task of cleaning into an Aroma therapy Session while breezing through the house. From kitchen to bath to windows, doors and floors, this all-purpose NATURAL cleaner covers all. Our potent essential oil enriched blend is safe to use in various ratios for virtually any cleaning task in you home.</p>
    <p>We unconditionally guarantee your sensory and cleaning satisfaction.<br><strong>More at Voldrimo.com</strong></p>
  </div>

  <div class="foliage foliage--green" role="img" aria-label="Green leaf sprigs" style="right:-30px;top:200px;width:110px;height:130px"></div>
  <div class="foliage foliage--soft" role="img" aria-label="Pale green leaf sprigs" style="left:-20px;top:260px;width:130px;height:100px"></div>

  <div class="claims">
    <div class="claims__col claims__col--yes">
      <h2 class="claims__head">Yes</h2>
      <ul class="claims__list">
        <li><svg width="7" height="6" viewBox="0 0 7 6"><path d="M0.5 3l2 2 4-4.5" fill="none" stroke="#a9c93b" stroke-width="1"/></svg>Non Toxic</li>
        <li><svg width="7" height="6" viewBox="0 0 7 6"><path d="M0.5 3l2 2 4-4.5" fill="none" stroke="#a9c93b" stroke-width="1"/></svg>Family &amp; Earth Friendly</li>
        <li><svg width="7" height="6" viewBox="0 0 7 6"><path d="M0.5 3l2 2 4-4.5" fill="none" stroke="#a9c93b" stroke-width="1"/></svg>Plant Based Natural Ingredients</li>
        <li><svg width="7" height="6" viewBox="0 0 7 6"><path d="M0.5 3l2 2 4-4.5" fill="none" stroke="#a9c93b" stroke-width="1"/></svg>Multi-purpose</li>
      </ul>
    </div>
    <div class="claims__divider"></div>
    <div class="claims__col claims__col--no">
      <h2 class="claims__head">No</h2>
      <ul class="claims__list">
        <li><svg width="6" height="6" viewBox="0 0 6 6"><path d="M1 1l4 4M5 1l-4 4" stroke="#d8342b" stroke-width="1"/></svg>Vinegar</li>
        <li><svg width="6" height="6" viewBox="0 0 6 6"><path d="M1 1l4 4M5 1l-4 4" stroke="#d8342b" stroke-width="1"/></svg>Phthalates</li>
        <li><svg width="6" height="6" viewBox="0 0 6 6"><path d="M1 1l4 4M5 1l-4 4" stroke="#d8342b" stroke-width="1"/></svg>Laurel Sulfates</li>
        <li><svg width="6" height="6" viewBox="0 0 6 6"><path d="M1 1l4 4M5 1l-4 4" stroke="#d8342b" stroke-width="1"/></svg>Preservatives</li>
        <li><svg width="6" height="6" viewBox="0 0 6 6"><path d="M1 1l4 4M5 1l-4 4" stroke="#d8342b" stroke-width="1"/></svg>Chemical Concoctions</li>
        <li><svg width="6" height="6" viewBox="0 0 6 6"><path d="M1 1l4 4M5 1l-4 4" stroke="#d8342b" stroke-width="1"/></svg>Dyes Synthetic Fragrance</li>
      </ul>
    </div>
  </div>

  <div class="back-rule"></div>
  <p class="ingredients"><strong>Ingredients:</strong> Water, Essential Oils: Cinnamon Leaf (cinnamomum zeylanicum), Clove (eugenia caryo-phyllata), Lemon (citrus limonum), Eucalyptus Globu- lus, Rosemary (rosemarinus officianales), Peppermint (mentha piperita), Sodium Cocoate, Vegetable Glycer-ine, Sodium Chloride, Sodium Gluconate, Citric Acid. Visit voldrimo.com for complete use and dilution guide.</p>
  <p class="warning">Keep out of reach of children. Stop use if irritation occurs. Keep out of eyes. For external use only</p>
</section>

</body>
</html>
```